添付の車の荷台部分とその際のドライブスルーのデザインになります。
合計2か所
添付のデザインイメージでお願いいたします。
・トラック看板寸法 3020×1800
・ドライブスルー看板 8280×1230
ドライブスルー看板のサイズが間違っていましたので、
再度はかってからまた記載させていただきます。

添付した写真「ドライブスルー 看板」が実際に使用する看板です。
ドライブスルーサイズ
誤りがありました!
正しくは

830×1230
です!

デザインが素敵でした。

今後ともよろしくお願いいたします。

```html
<!DOCTYPE html>
<html lang="ja">
<head>
<meta charset="utf-8">
<title>NOIR ドライブスルー看板</title>
<link rel="stylesheet" href="https://fonts.googleapis.com/css2?family=Poppins:wght@800&family=Noto+Sans+JP:wght@700;900&display=swap">
<style>
  :root {
    --ink: #000000;
    --cream: #fbf4c4;
  }
  * { margin: 0; padding: 0; box-sizing: border-box; }
  html, body {
    width: 808px;
    height: 1200px;
    overflow: hidden;
    background: var(--ink);
  }
  .sign {
    position: relative;
    width: 808px;
    height: 1200px;
    background: var(--ink);
    color: var(--cream);
  }
  .brand-mark {
    position: absolute;
    left: 334px;
    top: 190px;
    width: 140px;
    height: 140px;
    border-radius: 50%;
    background: var(--cream);
  }
  .brand-name {
    position: absolute;
    left: 0;
    right: 0;
    top: 470px;
    text-align: center;
    font-family: "Poppins", sans-serif;
    font-weight: 800;
    font-size: 150px;
    line-height: 1;
    letter-spacing: 2px;
  }
  .brand-tagline {
    position: absolute;
    left: 0;
    right: 0;
    top: 668px;
    text-align: center;
    font-family: "Noto Sans JP", sans-serif;
    font-weight: 700;
    font-size: 31px;
    letter-spacing: 0;
  }
  .direction-arrow {
    position: absolute;
    left: 0;
    top: 795px;
    width: 808px;
    height: 305px;
  }
  .direction-label {
    position: absolute;
    left: 180px;
    top: 905px;
    width: 520px;
    text-align: center;
    font-family: "Noto Sans JP", sans-serif;
    font-weight: 900;
    font-size: 72px;
    line-height: 1;
    color: var(--ink);
  }
</style>
</head>
<body>
  <main class="sign">
    <div class="brand-mark" aria-hidden="true"></div>
    <h1 class="brand-name">NOIR</h1>
    <p class="brand-tagline">炭サンドイッチ＆炭ばななジュース</p>
    <svg class="direction-arrow" viewBox="0 0 808 305" aria-hidden="true">
      <polygon points="0,152 160,0 160,80 808,80 808,228 160,228 160,305"
               fill="var(--cream)"/>
      <polyline points="14,152 148,26 148,92" fill="none" stroke="var(--ink)" stroke-width="3"/>
      <polyline points="14,152 148,279 148,216" fill="none" stroke="var(--ink)" stroke-width="3"/>
    </svg>
    <p class="direction-label">ドライブスルー</p>
  </main>
</body>
</html>
```